New Zealand Marlborough Sauvignon Blanc wine packaging design

We need packaging design for our new wine brand, Halloway Brisk. The wine is a New Zealand Marlborough Sauvignon Blanc. We would like the packaging will portray elegance and style with an understated label. We are looking for a label that portrays the elegance of the French Riviera. The label should be round or pill shaped.

Industry/Entity Type

Wine

Font styles to use
Serif
Sans Serif

Requirements
Must have
• The words in order of importance: Halloway Brisk, Sauvignon Blanc, Marlborough, New Zealand. It should be fit to the bottle posted in the links
Nice to have
• a pill shape or circular shape
Should not have
• Illustrations of wine bottles, wine glasses, or grapes

```html
<!DOCTYPE html>
<html lang="en">
<head>
<meta charset="utf-8">
<title>Halloway Brisk – Sauvignon Blanc Label</title>
<link rel="stylesheet" href="https://fonts.googleapis.com/css2?family=Cinzel:wght@700&family=Nunito+Sans:wght@400&display=swap">
<style>
  :root {
    --page-bg: #ece7e0;
    --label-bg: #2a2826;
    --label-edge: #35322f;
    --gold: #b48c4c;
    --gold-light: #cfa866;
    --gold-deep: #7a5a2c;
    --copper: #c07d42;
    --inner-disc: #262422;
  }
  html, body {
    margin: 0;
    padding: 0;
    width: 1125px;
    height: 1200px;
    overflow: hidden;
    background: var(--page-bg);
  }
  .canvas {
    position: relative;
    width: 1125px;
    height: 1200px;
  }
  .wine-label {
    position: absolute;
    left: 152px;
    top: 100px;
    width: 820px;
    height: 1000px;
    background: var(--label-bg);
    box-shadow: inset 0 0 0 1px var(--label-edge);
  }
  .wine-label svg {
    position: absolute;
    inset: 0;
    width: 100%;
    height: 100%;
  }
  .ornament-area {
    position: absolute;
    left: 87px;
    top: 259px;
    width: 642px;
    height: 512px;
    border-radius: 40%;
    background: radial-gradient(ellipse at center, rgba(180,140,76,0.55) 0%, rgba(150,112,56,0.35) 55%, rgba(42,40,38,0) 75%);
  }
  .seal-text {
    position: absolute;
    left: 0;
    width: 100%;
    text-align: center;
    margin: 0;
  }
  .brand-name {
    top: 498px;
    font-family: "Cinzel", serif;
    font-weight: 700;
    font-size: 36px;
    letter-spacing: 1px;
    color: var(--gold-light);
  }
  .region {
    top: 608px;
    font-family: "Nunito Sans", sans-serif;
    font-size: 21px;
    color: var(--gold);
  }
  .country {
    top: 650px;
    font-family: "Nunito Sans", sans-serif;
    font-size: 21px;
    letter-spacing: 1px;
    color: var(--gold);
  }
  .varietal {
    top: 830px;
    font-family: "Nunito Sans", sans-serif;
    font-size: 40px;
    letter-spacing: 2px;
    color: var(--copper);
  }
</style>
</head>
<body>
<main class="canvas">
  <section class="wine-label">
    <div class="ornament-area" role="img" aria-label="Gold baroque filigree scrollwork surrounding the central seal"></div>
    <svg viewBox="0 0 820 1000" aria-hidden="true">
      <g class="label-bands" stroke="#b48c4c" fill="none">
        <line x1="0" y1="362" x2="820" y2="362" stroke-width="3"/>
        <line x1="0" y1="374" x2="820" y2="374" stroke-width="1.5"/>
        <line x1="0" y1="432" x2="820" y2="432" stroke-width="1.5"/>
        <line x1="0" y1="444" x2="820" y2="444" stroke-width="3"/>
      </g>
      <circle class="seal-disc" cx="410" cy="520" r="222" fill="#262422"/>
      <circle class="seal-ring" cx="410" cy="520" r="222" fill="none" stroke="#b48c4c" stroke-width="7"/>
      <circle class="seal-ring-inner" cx="410" cy="520" r="206" fill="none" stroke="#b48c4c" stroke-width="2"/>
      <line class="name-rule" x1="245" y1="488" x2="575" y2="488" stroke="#7a5a2c" stroke-width="1.5"/>
      <line class="name-rule" x1="245" y1="560" x2="575" y2="560" stroke="#7a5a2c" stroke-width="1.5"/>
    </svg>
    <p class="seal-text brand-name">HALLOWAY BRISK</p>
    <p class="seal-text region">Marlborough</p>
    <p class="seal-text country">NEW ZEALAND</p>
    <p class="seal-text varietal">SAUVIGNON BLANC</p>
  </section>
</main>
</body>
</html>
```